Steadway Halvicor

We're designing a website to sell Halvicor Supplements. Attached is an image of the words we want to say and general layout, but please use your best knowledge to make it better. This platform is intentionally simplistic because this is reaching an older demographic, so it should be very straightforward, attention-grabbing and extremely user-friendly, while still appearing reliable and professional.
Use your best judgement for color palate that conveys professional but approachable. Feel free to add imagery but don't overwhelm the page.
Updates
Designs look the same
Target Market(s)
65+ seniors
Number of Pages Required
1 page
Look and feel

```html
<!DOCTYPE html>
<html lang="en">
<head>
<meta charset="utf-8">
<title>Steadway Halvicor</title>
<link href="https://fonts.googleapis.com/css2?family=Heebo:wght@500;700;800&family=Roboto:wght@300;400;500;700&display=swap" rel="stylesheet">
<style>
:root{
  --blue:#1b7fd0;
  --blue-dark:#0f66b6;
  --blue-light:#2d92de;
  --orange:#f26a12;
  --ink:#2b2b2b;
  --text:#555b63;
  --muted:#8a9099;
  --line:#e6e9ee;
  --section:#f2f4f8;
  --footer:#f8fafc;
}
*{box-sizing:border-box;margin:0;padding:0}
html,body{width:1200px;height:2432px;overflow:hidden}
body{position:relative;background:#fff;font-family:'Roboto',sans-serif;color:var(--text)}
.abs{position:absolute}
h1,h2,h3{font-family:'Heebo',sans-serif;color:var(--ink);letter-spacing:-0.5px}

/* header */
.site-header{position:absolute;left:0;top:0;width:1200px;height:64px;border-bottom:1px solid var(--line);background:#fff}
.brand{position:absolute;left:222px;top:14px;font:700 27px 'Roboto',sans-serif;color:var(--blue);letter-spacing:0.3px}
.brand span{color:var(--orange);font-weight:400}
.header-phone{position:absolute;left:703px;top:24px;font-size:11px;color:var(--ink);display:flex;align-items:center;gap:10px}
.header-divider{position:absolute;left:834px;top:18px;width:1px;height:26px;background:var(--line)}
.header-quotes{position:absolute;left:861px;top:26px;font-size:10px;font-weight:500;color:var(--orange);letter-spacing:0.3px}
.main-nav{position:absolute;left:0;top:64px;width:1200px;height:31px;display:flex}
.main-nav a{position:absolute;top:8px;font-size:12px;color:var(--ink);text-decoration:none}
.main-nav .active{left:221px;top:0;height:31px;padding:8px 12px 0;background:#f3f4f6;border-left:2px solid var(--orange);color:#555}

/* hero */
.hero{position:absolute;left:0;top:95px;width:1200px;height:463px;background:linear-gradient(90deg,#f4f7f9 0%,#e9eff3 40%,#dfe8ee 100%)}
.hero-photo{position:absolute;left:440px;top:0;width:760px;height:463px;background:linear-gradient(100deg,#e6edf1 0%,#9fc9cf 35%,#c9dbe4 60%,#eef3f6 100%)}
.hero h1{position:absolute;left:233px;top:66px;font-size:46px;font-weight:800;line-height:50px}
.hero-lead{position:absolute;left:235px;top:183px;font-size:20px;font-weight:300;color:var(--ink);line-height:32px}
.btn-primary{position:absolute;left:234px;top:263px;width:126px;height:32px;background:var(--orange);color:#fff;font-size:10px;font-weight:700;display:flex;align-items:center;justify-content:center;letter-spacing:0.2px}

/* plan cards */
.plan-card{position:absolute;top:504px;width:231px;height:218px;border-radius:4px;background:linear-gradient(160deg,var(--blue-light),var(--blue-dark));color:#fff;text-align:center;padding-top:50px}
.plan-card svg{display:block;margin:0 auto}
.plan-card h3{color:#fff;font-family:'Heebo',sans-serif;font-size:19px;font-weight:700;line-height:25px;margin-top:14px}
.plan-card p{font-size:9px;line-height:12.5px;padding:0 14px;margin-top:8px;opacity:.95}

/* about */
.about-art{position:absolute;left:0;top:768px;width:570px;height:349px;overflow:hidden}
.about-blob{position:absolute;left:-80px;top:0;width:620px;height:620px;border-radius:50%;background:linear-gradient(160deg,#eef6fd,#d4e6f8)}
.about-photo{position:absolute;left:245px;top:12px;width:300px;height:337px;border-radius:140px 140px 0 0;background:linear-gradient(180deg,#5a8fd6 0%,#6c98d5 45%,#4f7fc4 100%)}
.about h2{position:absolute;left:609px;top:758px;font-size:34px;font-weight:700}
.about-sub{position:absolute;left:609px;top:811px;font-size:11px;font-weight:300;color:var(--orange)}
.about ul{position:absolute;left:609px;top:843px;width:354px;list-style:none}
.about li{position:relative;padding-left:13px;font-size:10px;font-weight:300;line-height:15px;color:#444;margin-bottom:19px}
.about li::before{content:"";position:absolute;left:2px;top:5px;width:4px;height:4px;border-radius:50%;background:#9fd0f2}
.btn-outline{position:absolute;left:621px;top:1053px;width:83px;height:26px;border:1px solid #dcdfe4;border-radius:2px;color:var(--orange);font-size:8px;font-weight:500;display:flex;align-items:center;justify-content:center}

/* how it works */
.how{position:absolute;left:0;top:1117px;width:1200px;height:468px;background:var(--section)}
.how h2{position:absolute;left:0;top:44px;width:1200px;text-align:center;font-size:34px;font-weight:700}
.how-intro{position:absolute;left:234px;top:97px;width:732px;text-align:center;font-size:10px;font-weight:300;line-height:15px;color:#666}
.how-card{position:absolute;top:170px;width:169px;height:250px;background:#fff;border-bottom:2px solid #c9ccd2;padding:20px 12px 0}
.how-icon{width:60px;height:54px;margin:0 auto;border-radius:6px;background:linear-gradient(160deg,#e4ecf6,#cfdcec)}
.how-card h3{font-family:'Roboto',sans-serif;font-size:11px;font-weight:500;color:var(--ink);margin-top:22px;letter-spacing:0.3px;white-space:nowrap}
.how-card ul{list-style:none;margin-top:12px}
.how-card li{position:relative;padding-left:15px;font-size:8.5px;line-height:10.5px;color:#444;margin-bottom:5px;letter-spacing:0.2px}
.how-card li::before{content:"";position:absolute;left:0;top:1px;width:5px;height:5px;border-radius:50%;border:2px solid var(--orange)}
.more{position:absolute;left:12px;top:223px;width:74px;height:18px;border-radius:9px;border:1px solid #d8dbe0;font-size:7.5px;color:var(--orange);display:flex;align-items:center;justify-content:center}
.more.filled{background:var(--orange);border-color:var(--orange);color:#fff}

/* blog */
.blog h2{position:absolute;left:0;top:1640px;width:1200px;text-align:center;font-size:34px;font-weight:700;line-height:37px}
.post{position:absolute;top:1751px;width:231px;height:310px;background:#fff;border:1px solid #dfe2e6}
.post-photo{position:absolute;left:0;top:0;width:229px;height:147px}
.post-date{position:absolute;left:12px;top:131px;width:37px;height:46px;background:var(--orange);color:#fff;text-align:center;font-size:8px;padding-top:11px;line-height:12px}
.post-date b{display:block;font-size:11px;font-weight:500}
.post-read{position:absolute;left:61px;top:158px;font-size:10px;color:var(--orange)}
.post h3{position:absolute;left:11px;top:196px;font-family:'Roboto',sans-serif;font-size:10px;font-weight:500;color:var(--ink);letter-spacing:0.4px}
.post p{position:absolute;left:11px;top:221px;width:209px;font-size:7.5px;line-height:15px;color:#888}
.post-foot{position:absolute;left:11px;top:276px;width:207px;border-top:1px solid var(--line);padding-top:11px;font-size:7.5px;color:#999;letter-spacing:0.3px}

/* partners */
.partners{position:absolute;left:0;top:2120px;width:1200px;height:67px;background:linear-gradient(90deg,#1a78cd,#0f63b3);display:flex;align-items:center;justify-content:space-around;padding:0 130px}
.partner{display:flex;align-items:center;gap:8px;color:#fff;font-size:17px;font-weight:500}
.partner i{display:block;width:16px;height:16px;border-radius:50%;background:#fff}

/* footer */
.site-footer{position:absolute;left:0;top:2187px;width:1200px;height:245px;background:var(--footer)}
.site-footer h4{position:absolute;top:38px;font-size:10px;font-weight:500;color:var(--blue);letter-spacing:0.5px}
.foot-col{position:absolute;top:77px;font-size:7.5px;line-height:12.5px;color:#888}
.foot-links a{display:block;color:#888;text-decoration:none;margin-bottom:13px}
.social{position:absolute;left:796px;top:75px;display:flex;gap:13px}
.social i{display:block;width:21px;height:21px;border-radius:50%;background:#eef0f3}
.social i.on{background:var(--orange)}
.foot-brand{position:absolute;left:796px;top:123px;font-size:11px;color:var(--blue)}
.foot-mail{position:absolute;left:796px;font-size:7.5px;color:#888;display:flex;align-items:center;gap:12px}
.copyright{position:absolute;left:234px;top:2414px;font-size:8px;color:var(--orange)}
.foot-url{position:absolute;left:803px;top:2414px;font-size:8px;color:var(--orange)}
</style>
</head>
<body>

<header class="site-header">
  <div class="brand">Steadway <span>Halvicor</span></div>
  <div class="header-phone">
    <svg width="10" height="10" viewBox="0 0 24 24"><path fill="#5aa832" d="M6.6 10.8c1.4 2.8 3.8 5.1 6.6 6.6l2.2-2.2c.3-.3.7-.4 1-.2 1.1.4 2.3.6 3.6.6.6 0 1 .4 1 1V20c0 .6-.4 1-1 1C10.6 21 3 13.4 3 4c0-.6.4-1 1-1h3.5c.6 0 1 .4 1 1 0 1.3.2 2.5.6 3.6.1.3 0 .7-.2 1z"/></svg>
    (800) 555-0148
  </div>
  <div class="header-divider"></div>
  <div class="header-quotes">GET QUOTES</div>
</header>

<nav class="main-nav">
  <a class="active" href="#">Home</a>
  <a href="#" style="left:314px">About Us</a>
  <a href="#" style="left:413px">Services</a>
  <a href="#" style="left:509px">Blog</a>
  <a href="#" style="left:582px">Contact Us</a>
</nav>

<section class="hero">
  <div class="hero-photo" role="img" aria-label="Photo of four smiling medical staff in scrubs and white coats in a hospital corridor"></div>
  <h1>Find Your 2020<br>Halvicor Plan</h1>
  <p class="hero-lead">Easy. Effective. Get coverage<br>that's right for you.</p>
  <div class="btn-primary">CONTACT US NOW</div>
</section>

<div class="plan-card" style="left:234px">
  <svg width="46" height="40" viewBox="0 0 46 40" fill="none" stroke="#fff" stroke-width="2"><rect x="2" y="9" width="42" height="29" rx="3"/><path d="M16 9V4h14v5"/><path d="M23 16v15M15.5 23.5h15"/></svg>
  <h3>Halvicor<br>Supplement</h3>
  <p>Lorem ipsum dolor sit amet, consectetur adipi-scing elit, sed do eiusmod tempor incididunt ut labore et dolore magna aliqua.</p>
</div>
<div class="plan-card" style="left:484px">
  <svg width="40" height="40" viewBox="0 0 40 40" fill="none" stroke="#fff" stroke-width="2"><path d="M8 3v8a7 7 0 0 0 14 0V3"/><path d="M15 18v8a8 8 0 0 0 16 0v-4"/><circle cx="31" cy="18" r="4"/></svg>
  <h3>Halvicor<br>Part D</h3>
  <p>Lorem ipsum dolor sit amet, consectetur adipi-scing elit, sed do eiusmod tempor incididunt ut labore et dolore magna aliqua.</p>
</div>
<div class="plan-card" style="left:734px">
  <svg width="34" height="40" viewBox="0 0 34 40" fill="none" stroke="#fff" stroke-width="2"><rect x="2" y="2" width="30" height="36" rx="3"/><path d="M7 8h20"/><circle cx="17" cy="22" r="8"/><path d="M17 17v10M12 22h10"/></svg>
  <h3>Halvicor<br>Advantage</h3>
  <p>Lorem ipsum dolor sit amet, consectetur adipi-scing elit, sed do eiusmod tempor incididunt ut labore et dolore magna aliqua.</p>
</div>

<section class="about">
  <div class="about-art">
    <div class="about-blob"></div>
    <div class="about-photo" role="img" aria-label="Photo of a nurse in blue scrubs and cap holding a red stethoscope"></div>
  </div>
  <h2>About Us</h2>
  <div class="about-sub">Corvenda Health Communications Ltd.</div>
  <ul>
    <li>We are committed to make medical communications/solutions available for the clients for their growth.</li>
    <li>Total 15 years of experience in relation to medical writing, clinical research, communicating during CMEs, etc.</li>
    <li>Our services that would be of a great help for you are: solutions in the form of medical writing of scientific inputs/articles, Publications, clinical research, communicating during CMEs, etc.</li>
    <li>Support clients from industries viz. Pharmaceutical, Nutraceutical, Bio-technology, Medical devices, Hospital/Clinics.</li>
  </ul>
  <div class="btn-outline">READ MORE</div>
</section>

<section class="how">
  <h2>How Halvicor works</h2>
  <p class="how-intro">Lorem ipsum dolor sit amet, consectetur adipiscing elit, sed do eiusmod tempor incididunt ut labore et dolore magna aliqua. Ut enim ad minim veniam, quis nostrud exercitation ullamco laboris nisi ut aliquip ex ea commodo consequat. Duis aute irure dolor in reprehenderit in voluptate velit esse cillum dolore eu fugiat nulla pariatur. Excepteur sint occaecat cupidatat non proident, sunt in culpa qui offi id est laborum.</p>

  <div class="how-card" style="left:234px">
    <div class="how-icon" role="img" aria-label="Hospital building illustration"></div>
    <h3>Hospital &amp; Inpatient</h3>
    <ul><li>Hospital-related coverage</li><li>Emergency care</li><li>Skilled nursing</li><li>Home health services</li><li>Hospice</li></ul>
    <div class="more filled">More...</div>
  </div>
  <div class="how-card" style="left:421px">
    <div class="how-icon" role="img" aria-label="Doctor illustration"></div>
    <h3>Doctors &amp; Medical</h3>
    <ul><li>Doctor's office visits</li><li>Laboratory services</li><li>Medical equipment</li><li>Mental health services</li><li>Outpatient and ambulatory services</li></ul>
    <div class="more">More...</div>
  </div>
  <div class="how-card" style="left:609px">
    <div class="how-icon" role="img" aria-label="Hospital and doctor illustration"></div>
    <h3>Halvicor Advantage</h3>
    <ul><li>Lower monthly premium costs</li><li>Can only use in-network doctors and hospitals, and referred specialists</li><li>No coverage outside of local service area</li></ul>
    <div class="more">More...</div>
  </div>
  <div class="how-card" style="left:796px">
    <div class="how-icon" role="img" aria-label="Prescription bottle and pills illustration"></div>
    <h3>Halvicor Prescription...</h3>
    <ul><li>Part A + Part D</li><li>Part A + Part B + Part D</li><li>Part A + Part B + Supplement + Part D</li><li>An Advantage plan that includes Part D</li></ul>
    <div class="more">More...</div>
  </div>
</section>

<section class="blog">
  <h2>Recently Written By<br>Our Insurance Experts</h2>
  <article class="post" style="left:234px">
    <div class="post-photo" role="img" aria-label="Portrait photo of a smiling woman with curly hair" style="background:linear-gradient(135deg,#8fbf9a,#6a4a3a 55%,#c9b8a6)"></div>
    <div class="post-date">SEP<b>28</b></div>
    <div class="post-read">5 min read</div>
    <h3>MEMORY EXERCISES FOR SENIORS</h3>
    <p>Lorem Ipsum is simply dummy text of the printing and typesetting industry. Lorem Ipsum has been the industry's standard dummy text ever.</p>
    <div class="post-foot">READ MORE</div>
  </article>
  <article class="post" style="left:484px">
    <div class="post-photo" role="img" aria-label="Photo of a team meeting around an office table" style="background:linear-gradient(135deg,#3d4b5c,#7b6a58 55%,#a7876a)"></div>
    <div class="post-date">OCT<b>14</b></div>
    <div class="post-read" style="top:162px">9 min read</div>
    <h3>WAYS FOR SENIORS TO SAVE MONEY</h3>
    <p>It is a long established fact that a reader will be distracted by the readable content of a page when looking at its layout. The point of using Lorem .</p>
    <div class="post-foot">READ MORE</div>
  </article>
  <article class="post" style="left:734px">
    <div class="post-photo" role="img" aria-label="Photo of two colleagues reviewing charts on a laptop" style="background:linear-gradient(135deg,#e3e8ec,#2f4a72 55%,#dfe5ea)"></div>
    <div class="post-date">NOV<b>09</b></div>
    <div class="post-read">13 min read</div>
    <h3>HALVICOR AND VA BENEFITS</h3>
    <p>There are many variations of passages of Lorem Ipsum available, but the majority have suffered alteration in some form, by injected humour.</p>
    <div class="post-foot">READ MORE</div>
  </article>
</section>

<section class="partners">
  <div class="partner"><i></i>Lumora Labs</div>
  <div class="partner">Verdal Nutrition</div>
  <div class="partner">Brightel</div>
  <div class="partner"><i></i>Hollins, Marr &amp; Co.</div>
  <div class="partner">Kestrel Vita</div>
</section>

<footer class="site-footer">
  <h4 style="left:234px">INFO</h4>
  <h4 style="left:464px">QUICK LINKS</h4>
  <h4 style="left:608px">INFORMATION</h4>
  <h4 style="left:796px">GET IN TOUCH</h4>

  <div class="foot-col" style="left:234px;width:190px;display:flex;gap:6px">
    <svg width="7" height="10" viewBox="0 0 12 16" style="margin-top:2px;flex:none"><path fill="#666" d="M6 0a6 6 0 0 0-6 6c0 4.5 6 10 6 10s6-5.5 6-10a6 6 0 0 0-6-6zm0 8.5A2.5 2.5 0 1 1 6 3.5a2.5 2.5 0 0 1 0 5z"/></svg>
    <span>Suite 12, Orchard Court, 48 Millbrook<br>Road, Fairhaven Business Park,<br>near Riverside Clinic, off Elm<br>Avenue, North Quarter<br>Fairhaven 40210, Westland.</span>
  </div>
  <div class="foot-col" style="left:234px;top:160px;display:flex;gap:9px;align-items:center">
    <svg width="9" height="9" viewBox="0 0 24 24"><path fill="#666" d="M6.6 10.8c1.4 2.8 3.8 5.1 6.6 6.6l2.2-2.2c.3-.3.7-.4 1-.2 1.1.4 2.3.6 3.6.6.6 0 1 .4 1 1V20c0 .6-.4 1-1 1C10.6 21 3 13.4 3 4c0-.6.4-1 1-1h3.5c.6 0 1 .4 1 1 0 1.3.2 2.5.6 3.6.1.3 0 .7-.2 1z"/></svg>
    (800) 555-0148
  </div>

  <div class="foot-col foot-links" style="left:464px">
    <a href="#" style="color:var(--orange)">Contact Us</a>
    <a href="#">Blogs</a>
  </div>
  <div class="foot-col foot-links" style="left:608px">
    <a href="#">About Us</a>
    <a href="#">Privacy Policy</a>
    <a href="#">Terms &amp; Conditions</a>
    <a href="#">Contact Us</a>
  </div>

  <div class="social"><i></i><i class="on"></i><i></i></div>
  <div class="foot-brand">Steadway Halvicor</div>
  <div class="foot-mail" style="top:146px">
    <svg width="11" height="8" viewBox="0 0 22 16" fill="none" stroke="#666" stroke-width="1.6"><rect x="1" y="1" width="20" height="14"/><path d="M1 1l10 8 10-8"/></svg>
    info@steadway-example.com
  </div>
  <div class="foot-mail" style="top:165px">
    <svg width="11" height="8" viewBox="0 0 22 16" fill="none" stroke="#666" stroke-width="1.6"><rect x="1" y="1" width="20" height="14"/><path d="M1 1l10 8 10-8"/></svg>
    contact@steadway-example.com
  </div>
</footer>
<div class="copyright">© Copyright 2020. All Rights Reserved</div>
<div class="foot-url">www.steadway-example.com</div>

</body>
</html>
```